Real eatate

My company name is “Maple Crest Realestate” i would like to create a business card. I would like something modern and sleek similar to picture uploaded. All text in the business card should be black and the logo gold any shade.

```html
<!DOCTYPE html>
<html lang="en">
<head>
<meta charset="utf-8">
<title>Maple Crest Realestate – Business Card</title>
<link href="https://fonts.googleapis.com/css2?family=Oswald:wght@500&family=Open+Sans:wght@400&display=swap" rel="stylesheet">
<style>
  :root {
    --backdrop: #2b2b2c;
    --card: #f3f1ec;
    --pattern-light: #f6f4ef;
    --pattern-dark: #e4e1da;
    --gold: #f7b515;
    --text: #111112;
    --rule: #8c8a86;
    --icon-ink: #111112;
  }
  * { margin: 0; padding: 0; box-sizing: border-box; }
  html, body {
    width: 1200px; height: 1108px; overflow: hidden;
    background: var(--backdrop);
  }
  .stage {
    width: 1200px; height: 1108px;
    display: flex; justify-content: center; align-items: center; gap: 80px;
  }
  .card {
    width: 400px; height: 640px;
    background: var(--card);
    border-radius: 16px;
    box-shadow: 0 18px 40px rgba(0,0,0,.45);
    position: relative; overflow: hidden;
  }
  .card-front {
    display: flex; flex-direction: column; align-items: center;
    padding-top: 112px; color: var(--text);
    font-family: "Open Sans", Arial, sans-serif; text-align: center;
  }
  .brand {
    display: flex; align-items: center; gap: 14px;
    font-family: "Oswald", "Arial Narrow", sans-serif; font-weight: 500;
    color: var(--text); font-size: 34px; line-height: 1.12;
    text-transform: uppercase; text-align: left;
  }
  .brand-mark {
    width: 22px; height: 22px; border-radius: 50%; background: var(--gold); flex: none;
  }
  .person-name {
    margin-top: 72px;
    font-family: "Oswald", "Arial Narrow", sans-serif; font-weight: 500;
    font-size: 30px; color: var(--text); text-transform: uppercase; line-height: 1;
  }
  .person-role { font-size: 17px; margin-top: 6px; }
  .icon-row { display: flex; align-items: center; gap: 8px; margin-top: 16px; }
  .icon-row .rule { width: 40px; height: 1px; background: var(--rule); }
  .icon {
    width: 30px; height: 30px; border-radius: 5px; background: var(--gold);
    display: flex; align-items: center; justify-content: center;
  }
  .icon svg { width: 18px; height: 18px; }
  .contact-list { list-style: none; margin-top: 10px; font-size: 17px; line-height: 1.45; }
  .divider { width: 230px; height: 1px; background: var(--rule); margin: 12px 0; }
  .address { font-size: 17px; line-height: 1.4; font-style: normal; }
  .card-back { display: flex; align-items: center; justify-content: center; }
  .back-pattern {
    position: absolute; inset: 0;
    background: linear-gradient(160deg, var(--pattern-light) 0%, var(--pattern-dark) 100%);
  }
  .back-brand { position: relative; margin-top: 260px; font-size: 22px; }
  .back-brand .brand-mark { width: 14px; height: 14px; }
</style>
</head>
<body>
<main class="stage">
  <section class="card card-front" aria-label="Business card front">
    <div class="brand">
      <span class="brand-mark"></span>
      <span>Maple Crest<br>Realestate</span>
    </div>
    <h1 class="person-name">Daniel Harper</h1>
    <p class="person-role">Managing Director</p>
    <div class="icon-row">
      <span class="rule"></span>
      <span class="icon" aria-label="phone"><svg viewBox="0 0 24 24"><path fill="var(--icon-ink)" d="M6.6 10.8a15 15 0 0 0 6.6 6.6l2.2-2.2c.3-.3.7-.4 1-.2 1.1.4 2.3.6 3.6.6.6 0 1 .4 1 1V20c0 .6-.4 1-1 1A17 17 0 0 1 3 4c0-.6.4-1 1-1h3.5c.6 0 1 .4 1 1 0 1.3.2 2.5.6 3.6.1.3 0 .7-.2 1z"/></svg></span>
      <span class="icon" aria-label="mobile"><svg viewBox="0 0 24 24"><rect x="6" y="2" width="12" height="20" rx="2" fill="none" stroke="var(--icon-ink)" stroke-width="2"/><circle cx="12" cy="18" r="1.2" fill="var(--icon-ink)"/></svg></span>
      <span class="icon" aria-label="email"><svg viewBox="0 0 24 24"><rect x="3" y="5" width="18" height="14" rx="1" fill="none" stroke="var(--icon-ink)" stroke-width="2"/><path d="M3 6l9 7 9-7" fill="none" stroke="var(--icon-ink)" stroke-width="2"/></svg></span>
      <span class="icon" aria-label="website"><svg viewBox="0 0 24 24"><circle cx="12" cy="12" r="9" fill="none" stroke="var(--icon-ink)" stroke-width="2"/><path d="M3 12h18M12 3c3 3 3 15 0 18M12 3c-3 3-3 15 0 18" fill="none" stroke="var(--icon-ink)" stroke-width="1.6"/></svg></span>
      <span class="rule"></span>
    </div>
    <ul class="contact-list">
      <li>044-555 210 374</li>
      <li>044-555 210 386</li>
      <li>info@maplecrest-re.com</li>
      <li>www.maplecrest-re.com</li>
    </ul>
    <div class="divider"></div>
    <address class="address">87, Harbour View Road<br>20841, Portland</address>
  </section>

  <section class="card card-back" aria-label="Business card back">
    <div class="back-pattern" role="img" aria-label="Subtle tone-on-tone repeating brand pattern"></div>
    <div class="brand back-brand">
      <span class="brand-mark"></span>
      <span>Maple Crest</span>
    </div>
  </section>
</main>
</body>
</html>
```